Präsentationsvorlagen für eine internistisch-allgemeinmedizinische Arztpraxis
Zielgruppe
Wir sind eine internistisch-allgemeinmedizinische Arztpraxis
Die Folien werden sowohl für Fachvortröge aber auch für Patientenvorträge genutzt
Aufgabenstellung
Hätte gerne einen Vorschlag für 2 Versionen Format 16:9 und 4:3
Des Weiteren hätte ich gerne einen Bereich in der Präsentation wo man Studien/Literaturzutate ersichtlich darstellen kann.

```html
<!DOCTYPE html>
<html lang="de">
<head>
<meta charset="utf-8">
<title>Präsentationsvorlage 4:3 – Praxis am Lindenhof</title>
<link rel="stylesheet" href="https://fonts.googleapis.com/css2?family=Montserrat:wght@600;700&family=Open+Sans:wght@400;700;800&display=swap">
<style>
  :root {
    --brand-blue: #035f92;
    --brand-navy: #0a1450;
    --paper: #ffffff;
  }
  html, body {
    margin: 0;
    padding: 0;
    overflow: hidden;
    background: var(--brand-blue);
  }
  .slide {
    position: relative;
    width: 1200px;
    height: 900px;
    background: var(--brand-blue);
    overflow: hidden;
  }
  .brand-mark {
    position: absolute;
    left: 92px;
    top: 115px;
    width: 200px;
    height: 200px;
    border-radius: 50%;
    background: var(--paper);
  }
  .header-art {
    position: absolute;
    left: 0;
    top: 0;
  }
  .doctor-title,
  .doctor-name,
  .specialty {
    font-family: "Montserrat", sans-serif;
    fill: var(--paper);
  }
  .doctor-title { font-weight: 600; font-size: 38px; }
  .doctor-name { font-weight: 700; font-size: 59px; }
  .specialty { font-weight: 700; font-size: 28px; }
  .rule { stroke: var(--paper); stroke-width: 3; }
  .practice-name {
    font-family: "Open Sans", sans-serif;
    font-weight: 800;
    font-size: 72px;
    fill: var(--brand-navy);
  }
  .practice-doctors {
    font-family: "Open Sans", sans-serif;
    font-weight: 400;
    font-size: 21px;
    fill: var(--paper);
  }
  .practice-field {
    font-family: "Open Sans", sans-serif;
    font-weight: 700;
    font-size: 18px;
    fill: var(--paper);
  }
  .content-area {
    position: absolute;
    left: 348px;
    top: 507px;
    width: 487px;
    height: 309px;
    background: var(--paper);
  }
</style>
</head>
<body>
  <main class="slide">
    <div class="brand-mark" aria-hidden="true"></div>

    <svg class="header-art" width="1200" height="900" viewBox="0 0 1200 900" aria-label="Kopfbereich der Folie">
      <line class="rule" x1="351" y1="164" x2="477" y2="164"/>
      <line class="rule" x1="717" y1="164" x2="843" y2="164"/>
      <text class="doctor-title" x="597" y="176" text-anchor="middle">Dr. med.</text>

      <text class="doctor-name" x="350" y="228" textLength="493" lengthAdjust="spacingAndGlyphs">Tobias Tompelwick</text>

      <text class="specialty" x="350" y="266" textLength="493" lengthAdjust="spacingAndGlyphs">Facharzt für Innere-/Allgemein- und</text>
      <line class="rule" x1="351" y1="289" x2="440" y2="289"/>
      <line class="rule" x1="754" y1="289" x2="843" y2="289"/>
      <text class="specialty" x="597" y="298" text-anchor="middle">Ernährungsmedizin</text>

      <text class="practice-name" x="351" y="380" textLength="735" lengthAdjust="spacingAndGlyphs">Praxis am Lindenhof</text>

      <text class="practice-doctors" x="354" y="409" textLength="483" lengthAdjust="spacingAndGlyphs">Dr. med. Tobias Tompelwick | Dr. med. Jonas Brevik</text>
      <text class="practice-field" x="354" y="433" textLength="483" lengthAdjust="spacing">Innere- und Allgemeinmedizin</text>
    </svg>

    <section class="content-area" aria-label="Inhaltsbereich für Studien und Literaturzitate"></section>
  </main>
</body>
</html>
```